Website Online Research Solutions

We are a small European high-tech online research company.
With our own state of the art software we run online panels and are conducting reseach for companies. Partly research via our own panel and partly via panels we maintain for our customers.
Our current website is old and outdatet: www.pravelo.nl.
We are in the process to change the content of the site. We want a modern, european and businesslike design for our new website.
Our logo has to stay the same (left uppersite of our website and attached) but can be changed a little to adapt it to the new design of the website. The colors of the site are up to you.
Target Market(s)
Marketeers and researchers of large and middle size companies in all kind of fields.
Industry/Entity Type
Online
Look and feel
Each slider illustrates characteristics of the customer's brand and the style your logo design should communicate.

```html
<!DOCTYPE html>
<html lang="en">
<head>
<meta charset="utf-8">
<title>Pravelo – Online Research Solutions</title>
<link rel="stylesheet" href="https://fonts.googleapis.com/css2?family=Source+Sans+3:wght@400&family=Noto+Sans:wght@400&family=Arimo:wght@400&display=swap">
<style>
  :root {
    --bg-dark: #0d161d;
    --bg-glow: #2f4b5d;
    --panel-frame: #3a4248;
    --panel: #e5e5e5;
    --heading: #6b6b6b;
    --body-text: #1a1a1a;
    --muted: #7c7c7c;
    --nav-active: #8a2b2b;
    --white: #ffffff;
    --accent-blue: #1aa3d6;
    --footer-top: #1b355c;
    --footer-bottom: #2d5893;
    --photo-tone: #6d6f73;
    --sketch-tone: #d9d4c2;
    --thumb-frame: #7a7a7a;
  }
  * { margin: 0; padding: 0; box-sizing: border-box; }
  html, body { width: 1200px; height: 900px; overflow: hidden; }
  body {
    position: relative;
    background: radial-gradient(ellipse 700px 520px at 600px 40px, var(--bg-glow), var(--bg-dark) 100%);
    font-family: "Noto Sans", Verdana, sans-serif;
  }
  .brand {
    position: absolute; left: 125px; top: 32px;
    display: flex; align-items: center; gap: 10px;
    color: var(--white);
    font: 400 26px "Source Sans 3", sans-serif;
    text-decoration: none;
  }
  .brand-mark { width: 44px; height: 44px; border: 2px solid var(--white); border-radius: 50%; }
  .main-nav { position: absolute; top: 47px; right: 125px; display: flex; }
  .main-nav a {
    display: block; height: 28px; line-height: 28px; padding: 0 14px; margin-left: 5px;
    color: var(--white); text-decoration: none;
    font: 400 16px "Source Sans 3", sans-serif;
  }
  .main-nav a + a { margin-left: 6px; }
  .main-nav a.is-active { background: var(--nav-active); }
  .content-panel {
    position: absolute; left: 119px; top: 108px; width: 961px; height: 695px;
    background: var(--panel); border: 5px solid var(--panel-frame); border-radius: 6px;
  }
  .column-divider {
    position: absolute; left: 686px; top: 17px; width: 1px; height: 648px;
    background: linear-gradient(#8a8a8a, #8a8a8a 90%, transparent);
  }
  .post-title, .widget-title {
    position: absolute; font: 400 29px "Source Sans 3", sans-serif; color: var(--heading);
  }
  .post-media { position: absolute; border: 3px solid var(--thumb-frame); border-radius: 2px; }
  .media-photo { background: linear-gradient(160deg, #9aa0a6, var(--photo-tone) 55%, #3b3d40); }
  .media-sketch { background: var(--sketch-tone); }
  .media-rule {
    position: absolute; width: 2px;
    background: linear-gradient(transparent, #777 30%, #777 70%, transparent);
  }
  .post-excerpt {
    position: absolute; font-size: 12.4px; line-height: 15.6px; color: var(--body-text);
  }
  .more-link {
    position: absolute; font: 400 14px "Source Sans 3", sans-serif; color: var(--muted); text-decoration: none;
  }
  .recent-list { position: absolute; left: 703px; top: 78px; width: 240px; list-style: none; }
  .recent-list li {
    position: relative; padding-left: 18px; font-size: 12px; line-height: 15px; color: var(--body-text);
    margin-bottom: 11px;
  }
  .recent-list li svg { position: absolute; left: 0; top: 3px; }
  .widget-rule { position: absolute; left: 700px; top: 243px; width: 237px; height: 1px; background: #8a8a8a; }
  .gallery-thumb { position: absolute; top: 323px; width: 74px; height: 74px; background: var(--sketch-tone); }
</style>
</head>
<body>
  <header>
    <a class="brand" href="#"><span class="brand-mark"></span>Pravelo</a>
    <nav class="main-nav">
      <a class="is-active" href="#">HOME</a>
      <a href="#">ABOUT US</a>
      <a href="#">DEMOS</a>
      <a href="#">MEDIA</a>
      <a href="#">OUR CUSTOMERS</a>
      <a href="#">CONTACT</a>
    </nav>
  </header>

  <main class="content-panel">
    <article>
      <h2 class="post-title" style="left:25px;top:28px;">Maecenas tempor mattis diam sed rutrum!</h2>
      <div class="post-media media-photo" style="left:22px;top:95px;width:231px;height:149px;" role="img" aria-label="Photo of a business team around a meeting table"></div>
      <div class="media-rule" style="left:274px;top:97px;height:146px;"></div>
      <p class="post-excerpt" style="left:296px;top:96px;width:350px;">Lorem ipsum dolor sit amet, consectetur adipiscing elit. Maecenas tempor mattis diam sed rutrum. Nunc ligula libero, suscipit quis aliquam id, luctus ac neque. Phasellus non nibh eget quam condimentum ullamcor-per. Donec tristique dignissim nunc vel egestas. Praesent non dolor in nulla tempor blandit sit amet id mi. Etiam congue massa in ante commodo accumsan mattis tellus sollicitudin. Curabitur id magna non libero</p>
      <a class="more-link" href="#" style="left:579px;top:238px;">Read More...</a>
    </article>
    <article>
      <h2 class="post-title" style="left:25px;top:286px;">Duis nec feugiat erat...</h2>
      <div class="post-media media-sketch" style="left:22px;top:353px;width:149px;height:149px;" role="img" aria-label="Sketch of a crossed-out necktie"></div>
      <div class="media-rule" style="left:194px;top:355px;height:146px;"></div>
      <p class="post-excerpt" style="left:216px;top:354px;width:462px;">Lorem ipsum dolor sit amet, consectetur adipiscing elit. Maecenas tempor mattis diam sed rutrum. Nunc ligula libero, suscipit quis ali-quam id, luctus ac neque. Phasellus non nibh eget quam condimentum ullamcorper. Donec tristique dignissim nunc vel egestas. Praesent non dolor in nulla tempor blandit sit amet id mi. Etiam congue massa in ante commodo accumsan mattis tellus sollicitudin. Curabitur id magna non libero</p>
      <a class="more-link" href="#" style="left:579px;top:496px;">Read More...</a>
    </article>

    <div class="column-divider"></div>

    <aside>
      <h3 class="widget-title" style="left:703px;top:28px;">Recent Posts</h3>
      <ul class="recent-list">
        <li><svg width="10" height="10" viewBox="0 0 10 10"><rect width="10" height="10" rx="2" fill="#1aa3d6"/><path d="M4 2.5 6.5 5 4 7.5" stroke="#fff" stroke-width="1.6" fill="none"/></svg>Maecenas tempor mattis diam sed</li>
        <li><svg width="10" height="10" viewBox="0 0 10 10"><rect width="10" height="10" rx="2" fill="#1aa3d6"/><path d="M4 2.5 6.5 5 4 7.5" stroke="#fff" stroke-width="1.6" fill="none"/></svg>Morbi sit amet vulputate est.</li>
        <li><svg width="10" height="10" viewBox="0 0 10 10"><rect width="10" height="10" rx="2" fill="#1aa3d6"/><path d="M4 2.5 6.5 5 4 7.5" stroke="#fff" stroke-width="1.6" fill="none"/></svg>Pellentesque convallis, felis at porttitor</li>
        <li><svg width="10" height="10" viewBox="0 0 10 10"><rect width="10" height="10" rx="2" fill="#1aa3d6"/><path d="M4 2.5 6.5 5 4 7.5" stroke="#fff" stroke-width="1.6" fill="none"/></svg>Morbi sit amet vulputate est.</li>
      </ul>
      <a class="more-link" href="#" style="left:875px;top:198px;">Show All</a>
      <div class="widget-rule"></div>
      <h3 class="widget-title" style="left:703px;top:270px;">Gallery</h3>
      <div class="gallery-thumb" style="left:705px;" role="img" aria-label="Gallery image: crossed-out necktie sketch"></div>
      <div class="gallery-thumb" style="left:785px;" role="img" aria-label="Gallery image: crossed-out necktie sketch"></div>
      <div class="gallery-thumb" style="left:864px;" role="img" aria-label="Gallery image: crossed-out necktie sketch"></div>
      <a class="more-link" href="#" style="left:850px;top:419px;">See them all!</a>
    </aside>
  </main>

  <footer style="position:absolute;left:0;top:830px;width:1200px;height:70px;background:linear-gradient(var(--footer-top),var(--footer-bottom));border-top:1px solid #4f6f99;font-family:Arimo,Arial,sans-serif;color:var(--white);font-size:12px;">
    <span style="position:absolute;left:141px;top:30px;">Pravelo 2010 © All rights reserved.</span>
    <span style="position:absolute;left:338px;top:26px;width:1px;height:22px;background:#6f8fb8;"></span>
    <a href="#" style="position:absolute;left:352px;top:30px;color:var(--white);">Privacy Policy</a>
    <address style="position:absolute;left:497px;top:21px;font-style:normal;line-height:19px;">Lindengracht 12 1531 KD Wormerveer<br>+31 (0)75 418 2260 - info@pravelo.nl</address>
    <span style="position:absolute;left:727px;top:24px;width:30px;height:30px;border-radius:4px;background:#3b5a9a;"></span>
    <span style="position:absolute;left:768px;top:24px;width:30px;height:30px;border-radius:4px;background:#5cc4e8;"></span>
    <span style="position:absolute;left:808px;top:24px;width:30px;height:30px;border-radius:4px;background:#ee7d1e;"></span>
    <form style="position:absolute;left:855px;top:19px;width:225px;height:40px;background:#fff;border:2px solid #9aa8b8;border-radius:4px;">
      <input type="text" placeholder="Search..." style="position:absolute;left:12px;top:9px;width:160px;border:0;outline:0;font:14px Arimo,Arial,sans-serif;color:#333;background:transparent;">
      <span style="position:absolute;right:0;top:0;width:40px;height:36px;background:linear-gradient(#f4f4f4,#d8dde3);border-left:1px solid #bbb;"></span>
      <svg style="position:absolute;right:9px;top:7px;" width="22" height="22" viewBox="0 0 22 22"><circle cx="9" cy="9" r="6.5" fill="#cfe6f7" stroke="#5b7a99" stroke-width="2"/><path d="M14 14 20 20" stroke="#5b7a99" stroke-width="3" stroke-linecap="round"/></svg>
    </form>
  </footer>
</body>
</html>
```